Wine label design for a family winery in Slovenia

We need new label design for our wines.
We are small family wine producers who focuses on good quality wine and loves to experiment, mixing tradition with new, more modern approaches. Our main product is ‘Teran’, red wine whose character is highly defined by terroir: more acidic, but rich body and very rich, dark colour (we say it's not red, but black). We also age a small portion of this Teran wine with wood, which we named 'Pelmik' (after one of our vineyards). From the same grapes as Teran we also produce a small quantity of Rose. And we also produce two white wine varieties: one is 'Sopa', cuvee of several different sorts of grapes. The other is 'Ostrena', Chardonnay wine, named after another of our vineyards. Aside from all that we also produce liquour (Teranov liker) made from Teran wine and a small quantity of other spirits (Grappa, various fruit liquors, a version of Blaustrummer, and ‘Travarica’ which is grappa infused with various herbs and spices).
Sopa, Rose and Teran are considered our 'basic' line, whereas 'Pelmik' and 'Ostrena' are considered to be a higher quality line. Rose sits somewhere between this two.
In time we'd like to renew all of our labels. But the priority and subject of this ‘’project’’ is to create the two for our top line, Pelmik and Ostrena and also for Rose.
For 'Pelmik' we already have a template label. The general idea behind it was play with letters and divide them along the label (PE LM IK). We found that we like the narrow, longer dimensions and that black label on black bottle, with letters that stand out due to colour or printing differences, work very well. But we're amateurs and the label is not finalized. We would ask you to do something on this basis, but please don't limit yourself only to this if you have a better idea.
For 'Ostrena' the label should be in the same style to imply the same higher quality line - colours can and probably should be reversed to the lighter side (so to imply that it’s a white wine). Also, for this wine we'll use the same dark slender bottles, like you see on the image.
Please keep in mind that we'll print smaller series (1000-2000 pcs), so it must be possible to print the labels for a sensible cost. Solutions like classical offset gold print that requires large series of 10.000 pcs, will not work. But we can look into any digital printing/lacquering options that offer similar effects. Anyway, we are not experts on this field, so your advice on printing techniques is also welcomed.
Also, a word on our emblem: the logo is also not finalized and we will also ask you to work on it. The logo is part of the ornament on the doors of our homestead and represents a ‘kolovrat’ (‘spinning wheel’ in English), an old Slavic symbol for the sun, representing eternal life and spinning of time. We'd like to use it, but right now it's badly digitalized. If you'll need any better photos of it, let me know.

Target Market(s)

30-60 yo, red wine lovers, appreciate local and speicality wines

Font styles to use
Sans Serif
Decorative

Requirements
Must have
• long, narrow label dimensions (see attached Pelmik)

```html
<!DOCTYPE html>
<html lang="sl">
<head>
<meta charset="utf-8">
<title>Kamnita Klet Dolan – Wine Labels</title>
<link rel="stylesheet" href="https://fonts.googleapis.com/css2?family=Marcellus&family=Marcellus+SC&display=swap">
<style>
  :root {
    --backdrop: #1c1c1c;
    --sheet: #ffffff;
    --label-dark: #2b2728;
    --label-light: #ffffff;
    --gold: #b5975c;
    --gold-soft: rgba(181, 151, 92, 0.28);
    --gold-dim: #6f624a;
    --grey-letter: #c9c9c9;
    --rose: #eaa3a3;
    --wine-red: #8c1c1c;
    --ink-dark: #3a3333;
    --ink-light: #e9e2d3;
  }
  * { box-sizing: border-box; margin: 0; padding: 0; }
  html, body { width: 1200px; height: 2179px; overflow: hidden; }
  body {
    background: var(--backdrop);
    font-family: "Marcellus", serif;
    position: relative;
  }
  .sheet {
    position: absolute;
    left: 127px;
    width: 947px;
    height: 668px;
    background: var(--sheet);
  }
  .sheet--pelmik { top: 28px; }
  .sheet--ostrena { top: 754px; }
  .sheet--rosnica { top: 1481px; }

  .label {
    position: absolute;
    top: 94px;
    width: 223px;
    height: 480px;
    overflow: hidden;
    box-shadow: 4px 6px 10px rgba(0,0,0,0.28);
  }
  .label--front { left: 333px; }
  .label--back { left: 584px; }
  .theme-dark { background: var(--label-dark); color: var(--ink-light); }
  .theme-light { background: var(--label-light); color: var(--ink-dark); }

  .vine-art {
    position: absolute;
    background: radial-gradient(ellipse at 45% 40%, var(--gold-soft), rgba(181,151,92,0.08) 65%, transparent 80%);
  }
  .label--front .vine-art { left: 10px; top: 0; width: 200px; height: 360px; }
  .label--back .vine-art.left { left: 0; top: 0; width: 70px; height: 200px; }
  .label--back .vine-art.right { right: 0; top: 170px; width: 60px; height: 310px; }

  .name-grid {
    position: absolute;
    left: 30px; top: 149px;
    width: 146px; height: 118px;
    border: 2px solid var(--gold);
    padding: 8px 6px 0;
    font-size: 31px;
    line-height: 34px;
    letter-spacing: 5px;
    text-align: center;
  }
  .name-grid .row { display: block; white-space: nowrap; }
  .theme-dark .name-grid .lit { color: var(--gold); }
  .theme-dark .name-grid .dim { color: var(--gold-dim); }
  .theme-light .name-grid .lit { color: var(--gold); }
  .theme-light .name-grid .dim { color: var(--grey-letter); }
  .theme-light .name-grid .blush { color: var(--rose); }

  .brand {
    position: absolute;
    left: 0; right: 0;
    text-align: center;
  }
  .brand-dot {
    display: block;
    margin: 0 auto 6px;
    width: 34px; height: 34px;
    border-radius: 50%;
    background: var(--wine-red);
  }
  .brand-name {
    font-family: "Marcellus SC", serif;
    font-size: 13px;
    line-height: 13px;
    color: var(--wine-red);
  }
  .theme-dark .brand-name { color: #f3efe7; }
  .label--front .brand { top: 358px; }

  .band {
    position: absolute;
    left: 0; right: 0;
    top: 450px;
    height: 13px;
    background: var(--wine-red);
    color: #f1dede;
    font-size: 6.5px;
    line-height: 13px;
    letter-spacing: 0.6px;
    text-align: center;
  }

  .back-frame {
    position: absolute;
    left: 46px; top: 46px;
    width: 134px; height: 388px;
    border: 1.5px solid var(--gold);
    text-align: center;
  }
  .theme-light .back-frame { background: var(--label-light); }
  .theme-dark .back-frame { background: var(--label-dark); }
  .back-frame .brand { top: 20px; }
  .back-frame .brand-dot { width: 28px; height: 28px; margin-bottom: 4px; }
  .back-frame .brand-name { font-size: 11px; line-height: 11px; }
  .spec { position: absolute; left: 0; right: 0; top: 102px; }
  .spec .region { font-size: 7.5px; letter-spacing: 0.4px; }
  .spec .wine-name { font-size: 19px; letter-spacing: 1px; margin-top: 4px; line-height: 20px; }
  .spec .variety { font-size: 10px; letter-spacing: 0.6px; }
  .spec .detail { font-size: 7.5px; line-height: 11px; }
  .story {
    position: absolute; left: 6px; right: 6px; top: 198px;
    font-size: 6.8px; line-height: 12px; letter-spacing: 0.3px;
  }
  .contact {
    position: absolute; left: 6px; right: 6px; top: 298px;
    font-size: 6.8px; line-height: 12px; letter-spacing: 0.3px;
  }
</style>
</head>
<body>

<!-- Pelmik: dark label for aged Teran -->
<section class="sheet sheet--pelmik">
  <article class="label label--front theme-dark">
    <div class="vine-art" role="img" aria-label="Gold line engraving of a grape cluster with vine leaves"></div>
    <div class="name-grid">
      <span class="row"><span class="lit">PE</span><span class="dim">LM</span></span>
      <span class="row"><span class="dim">E</span><span class="lit">LMI</span></span>
      <span class="row"><span class="dim">LM</span><span class="lit">IK</span></span>
    </div>
    <div class="brand"><span class="brand-dot"></span><div class="brand-name">Kamnita Klet<br>Dolan</div></div>
    <div class="band">LOREM IPSUM DOLOR SIT AMET</div>
  </article>
  <article class="label label--back theme-dark">
    <div class="vine-art left" role="img" aria-label="Gold line engraving of grapes"></div>
    <div class="vine-art right" role="img" aria-label="Gold line engraving of vine leaves"></div>
    <div class="back-frame">
      <div class="brand"><span class="brand-dot"></span><div class="brand-name">Kamnita Klet<br>Dolan</div></div>
      <div class="spec">
        <div class="region">VINORODNI OKOLIŠ KRAS</div>
        <div class="wine-name">PELMIK</div>
        <div class="variety">TERAN PTP</div>
        <div class="detail">SUHO VINO<br>2017</div>
      </div>
      <p class="story">IZDELAN PO TRADICIONALNEM POSTOPKU IZ IZBRANEGA GROZDJA TERANOVK S DOLANOVIH STARIH BRAJD NA PELMIKU</p>
      <p class="contact">KAMNITA KLET DOLAN<br>GORICA 14, 6220 LIPJE<br>KRAS, SLOVENIJA<br>KAMNITAKLETDOLAN.SI</p>
    </div>
  </article>
</section>

<!-- Ostrena: light label for Chardonnay -->
<section class="sheet sheet--ostrena">
  <article class="label label--front theme-light">
    <div class="vine-art" role="img" aria-label="Gold line engraving of a grape cluster with vine leaves"></div>
    <div class="name-grid">
      <span class="row"><span class="lit">OS</span><span class="dim">TR</span></span>
      <span class="row"><span class="dim">STR</span><span class="lit">EN</span></span>
      <span class="row"><span class="dim">TR</span><span class="lit">ENA</span></span>
    </div>
    <div class="brand"><span class="brand-dot"></span><div class="brand-name">Kamnita Klet<br>Dolan</div></div>
    <div class="band"></div>
  </article>
  <article class="label label--back theme-light">
    <div class="vine-art left" role="img" aria-label="Gold line engraving of grapes"></div>
    <div class="vine-art right" role="img" aria-label="Gold line engraving of vine leaves"></div>
    <div class="back-frame">
      <div class="brand"><span class="brand-dot"></span><div class="brand-name">Kamnita Klet<br>Dolan</div></div>
      <div class="spec">
        <div class="region">VINORODNI OKOLIŠ KRAS</div>
        <div class="wine-name">OSTRENA</div>
        <div class="variety">TERAN PTP</div>
        <div class="detail">SUHO VINO<br>2017</div>
      </div>
      <p class="story">IZDELAN PO TRADICIONALNEM POSTOPKU IZ IZBRANEGA GROZDJA TERANOVK S DOLANOVIH STARIH BRAJD NA PELMIKU</p>
      <p class="contact">KAMNITA KLET DOLAN<br>GORICA 14, 6220 LIPJE<br>KRAS, SLOVENIJA<br>KAMNITAKLETDOLAN.SI</p>
    </div>
  </article>
</section>

<!-- Rosnica: light label for Rose -->
<section class="sheet sheet--rosnica">
  <article class="label label--front theme-light">
    <div class="vine-art" role="img" aria-label="Gold line engraving of a grape cluster with vine leaves"></div>
    <div class="name-grid">
      <span class="row"><span class="lit">RO</span><span class="blush">SN</span></span>
      <span class="row"><span class="blush">S</span><span class="lit">NI</span><span class="blush">C</span></span>
      <span class="row"><span class="blush">NI</span><span class="lit">CA</span></span>
    </div>
    <div class="brand"><span class="brand-dot"></span><div class="brand-name">Kamnita Klet<br>Dolan</div></div>
    <div class="band">LOREM IPSUM DOLOR SIT AMET</div>
  </article>
  <article class="label label--back theme-light">
    <div class="vine-art left" role="img" aria-label="Gold line engraving of grapes"></div>
    <div class="vine-art right" role="img" aria-label="Gold line engraving of vine leaves"></div>
    <div class="back-frame">
      <div class="brand"><span class="brand-dot"></span><div class="brand-name">Kamnita Klet<br>Dolan</div></div>
      <div class="spec">
        <div class="region">VINORODNI OKOLIŠ KRAS</div>
        <div class="wine-name">ROSNICA</div>
        <div class="variety">TERAN PTP</div>
        <div class="detail">SUHO VINO<br>2017</div>
      </div>
      <p class="story">IZDELAN PO TRADICIONALNEM POSTOPKU IZ IZBRANEGA GROZDJA TERANOVK S DOLANOVIH STARIH BRAJD NA PELMIKU</p>
      <p class="contact">KAMNITA KLET DOLAN<br>GORICA 14, 6220 LIPJE<br>KRAS, SLOVENIJA<br>KAMNITAKLETDOLAN.SI</p>
    </div>
  </article>
</section>

</body>
</html>
```